Fantastische (!) Zusammenarbeit!! Reibungslose und schnelle Kommunikation. Änderungswünsche werden sofort entgegengenommen und umgesetzt. Soweit etwas nicht passt, wird so lange weiterverändert, bis es passt. Einfach super. Nachfragen werden binnen kürzester Zeit beantwortet - auch für allgemeine Fragen ein super Ansprechpartner. Danke hierfür ! Auch nach Ablauf des Projektes ist der Designer jederzeit ansprechbar und gibt gerne Hilfestellung. So stellt man sich Service vor! Ich kann KP47 wärmstens empfehlen. Jederzeit wieder. Die Rundum-Leistung ist klasse und das Endprodukt ohnehin super ! Nochmal herzlichen Dank!
Zielgruppe
Derzeit befinde ich mich in der Gründungsphase einer Softwarefirma namens 'Braukon-Solutions'. Nach der Namensfindung wird nun ein Corporate-Design benötig, bestehend aus einem ansprechendem Logo mit Wiedererkennungswert, einem Briefpapier für Korrespondenz und Rechnungen, sowie einer Visitenkarte inkl. QR-Code.
Tätigkeit:
Software- und Datenbankentwicklung für Firmenkunden
Zielgruppen:
sämtliche Firmen, die individuelle Softwarelösungen suchen
Was sind wir - folgende Merkmale sollen mit dem Logo visualisiert werden.
engagiert
- weil die Interessen der Kunden immer im Fokus der Zusammenarbeit stehen.
kompetent
- weil wir über hohes fachliches Know-How verfügen.
flexibel
- weil die Braukon-Solutions durch ein kleines, professionelles Team auf veränderte
Situationen sofort reagieren kann.
qualitätsbewusst
- weil die Braukon-Solutions keine Kompromisse macht wenn es um die Beratung und
Betreuung ihrer Kunden geht.
verlässlich
- weil langfristige und vertrauensvolle Beziehungen zu Geschäftspartnern zu den Grundprinzipiens unseres Handelns gehört.
unkonventionell und individuell
- weil die Braukon-Solutions immer bereit ist, im Interesse ihrer Kunden zu handeln
und unkonventionelle nicht zwingend branchentypische Lösungen zu schaffen.
Aufgabenstellung
Das Design soll klar strukturiert, modern und professionell sein. Kommuniziert werden sollen Vertrauen, Kompetenz, partnerschaftliche Zusammenarbeit, Individualität und Verlässlichkeit.
Bestehend aus einem ansprechendem Logo mit Wiedererkennungswert, einem Briefpapier für Korrespondenz und Rechnungen, sowie einer Visitenkarte inkl. QR-Code.

```html
<!DOCTYPE html>
<html lang="de">
<head>
<meta charset="utf-8">
<title>Braukon Solutions – Geschäftsausstattung</title>
<link href="https://fonts.googleapis.com/css2?family=Quicksand:wght@500;600&family=Roboto:wght@400;500;700&display=swap" rel="stylesheet">
<style>
  :root {
    --slate: #3b4250;
    --slate-deep: #353b48;
    --lime: #9bc03a;
    --paper: #ffffff;
    --ink: #2a2d33;
    --backdrop: #e9eaec;
  }
  * { box-sizing: border-box; margin: 0; padding: 0; }
  html, body { width: 1200px; height: 856px; overflow: hidden; }
  body { background: var(--backdrop); position: relative; font-family: 'Roboto', Arial, sans-serif; color: var(--ink); }

  .wordmark { display: flex; align-items: center; gap: 5px; font-family: 'Quicksand', Arial, sans-serif; font-weight: 600; color: var(--slate); white-space: nowrap; }
  .wordmark__square { display: block; background: var(--lime); flex: none; }
  .wordmark--light { color: var(--paper); }

  /* Letterhead */
  .letterhead { position: absolute; left: 177px; top: 133px; width: 415px; height: 588px; background: var(--paper); box-shadow: 0 6px 18px rgba(0,0,0,.18); }
  .letterhead .wordmark { position: absolute; right: 40px; top: 58px; font-size: 15px; }
  .letterhead .wordmark__square { width: 10px; height: 10px; }
  .sender-line { position: absolute; left: 44px; top: 90px; font-size: 4px; font-weight: 700; border-bottom: 0.6px solid var(--ink); padding-bottom: 1px; letter-spacing: .05px; }
  .recipient { position: absolute; left: 44px; top: 108px; font-size: 6.2px; line-height: 8px; }
  .recipient .city { margin-top: 8px; }
  .subject { position: absolute; left: 44px; top: 201px; font-size: 6.2px; font-weight: 700; }
  .letter-body { position: absolute; left: 44px; top: 224px; width: 228px; font-size: 5.9px; line-height: 7.55px; text-align: justify; }
  .letter-body p + p { margin-top: 7px; }
  .closing { position: absolute; left: 44px; top: 419px; font-size: 6px; }
  .signature { position: absolute; left: 44px; top: 437px; width: 86px; height: 18px; background: linear-gradient(90deg, #d9dbdf, #eceef0); border-radius: 2px; }
  .signer { position: absolute; left: 44px; top: 462px; font-size: 6px; }
  .letter-footer { position: absolute; left: 0; bottom: 0; width: 100%; height: 57px; background: var(--slate); color: #e6e8ec; font-family: 'Quicksand', Arial, sans-serif; font-size: 4.3px; letter-spacing: .35px; line-height: 7px; }
  .footer-col { position: absolute; top: 17px; transform: translateX(-50%); text-align: center; white-space: nowrap; }
  .footer-col--address { left: 116px; }
  .footer-col--contact { left: 212px; text-align: left; }
  .footer-col--bank { left: 307px; }
  .icon { display: inline-block; vertical-align: middle; }

  /* Business cards */
  .card { position: absolute; left: 769px; width: 253px; height: 163px; box-shadow: 0 6px 16px rgba(0,0,0,.2); overflow: hidden; }
  .card--front { top: 221px; background: var(--slate); }
  .card__head { height: 92px; background: var(--paper); display: flex; align-items: center; justify-content: center; }
  .card__head .wordmark { font-size: 16px; }
  .card__head .wordmark__square { width: 10px; height: 10px; }
  .card__details { font-family: 'Quicksand', Arial, sans-serif; color: #e6e8ec; font-size: 6.2px; letter-spacing: .5px; text-align: center; line-height: 9px; padding-top: 11px; }
  .card__details .accent { color: var(--lime); }
  .card__details .row { display: flex; justify-content: center; align-items: center; gap: 4px; }
  .card__details .web { margin-top: 5px; color: var(--lime); letter-spacing: 1px; }
  .card--back { top: 470px; background: var(--slate); display: flex; align-items: center; justify-content: center; }
  .card--back .wordmark { font-size: 17px; }
  .card--back .wordmark__square { width: 11px; height: 11px; }
</style>
</head>
<body>

<svg width="0" height="0" style="position:absolute">
  <defs>
    <symbol id="i-pin" viewBox="0 0 10 10"><rect x=".5" y=".5" width="9" height="9" rx="2" fill="none" stroke="#9bc03a"/><path d="M5 2.3a1.8 1.8 0 0 1 1.8 1.8C6.8 5.5 5 7.6 5 7.6S3.2 5.5 3.2 4.1A1.8 1.8 0 0 1 5 2.3z" fill="none" stroke="#9bc03a" stroke-width=".7"/></symbol>
    <symbol id="i-mail" viewBox="0 0 10 10"><rect x=".5" y=".5" width="9" height="9" rx="2" fill="none" stroke="#9bc03a"/><rect x="2.3" y="3.2" width="5.4" height="3.6" fill="none" stroke="#9bc03a" stroke-width=".7"/><path d="M2.3 3.2L5 5.3l2.7-2.1" fill="none" stroke="#9bc03a" stroke-width=".7"/></symbol>
    <symbol id="i-phone" viewBox="0 0 10 10"><rect x=".5" y=".5" width="9" height="9" rx="2" fill="none" stroke="#9bc03a"/><path d="M3.3 2.5l1 1.3-.6.7c.4.9 1 1.5 1.8 1.8l.7-.6 1.3 1-.6 1C5 7.6 2.4 5 2.4 3.1z" fill="none" stroke="#9bc03a" stroke-width=".6"/></symbol>
  </defs>
</svg>

<section class="letterhead">
  <div class="wordmark"><span class="wordmark__square"></span>Braukon Solutions</div>
  <div class="sender-line">Vorname Nachname, Musterstr. 123, 12345 Musterstadt</div>
  <div class="recipient">
    <div>Martina Musterfrau</div>
    <div>Musterstraße 456</div>
    <div class="city">12345 Berlin</div>
  </div>
  <div class="subject">Quidero molore, atatur sae. Nequat,</div>
  <div class="letter-body">
    <p>Ur sit, imus, ipicatem voluptate eum re dolluptios sequosam, eum reritati am volor sapedissi quo blaboribust, sequass itasped igendi cus exerfer feruptas iusanda ndaest, qui omnis nus aut fugitinis quatur ad ullaut mostem quasperiae corem et aciatem illatin ciduntores quidis utemquam autemperae soluptiae lab illacescia solorum et fugiam ratatatus exerro blaciis samusam etur? Uga. Neque nam simi, nest, ommod essedios magnatia nossi aute nonsequam fugiaspis moluptas sed el int etur saepe nonsecatem excea noneceperrum ulligendit faccullores et lantur si ium at. Ota cuptae non ea de opta voles rem rae dolore ilia vellab isi blanis idit veribus auda alit labore desenis imenis que in con rehent, explat ped que volorum, autent, si tetur?</p>
    <p>Ihil ium restior ecepero reptistius es aborepe diatiunt dignis diciae voluptu ribearit, que nat aute et as maximus, qui blab iur aut volest, nonsequae odios doluptatiae velignimin perescia vent. Pa voluptas expero corectur molest eaquid enda vidus verciis quodi te dit aliquid unturem poreper feratur? Quis aut rehenihilit et quam, eris et perorru mquamusa quo et untia volupie nisimoluptae esseribus cora doluptati doluptatur atisciumqui re pa quat aut lam solescia intiis et millabor sit odis et quos re sam, vendicientur abo. Equi totatus rest, nosam quodi omni doloriosam des ea nimpelique volo elendae dellign ihilitis solupta temporp orupta iuntia ipiste natibusapis volesedis reriori taerrup tatiberes nobitiur, sequi omnihillab id maximagnat omnimus dolo quunt, int aut earum lacit peliquunt iduciet, id que autemolum deruptati te non re.</p>
  </div>
  <div class="closing">Sincerely</div>
  <div class="signature" role="img" aria-label="Handschriftliche Unterschrift"></div>
  <div class="signer">Max Mustermann</div>
  <footer class="letter-footer">
    <div class="footer-col footer-col--address">
      Vorname Nachname<br>
      <svg class="icon" width="5" height="5"><use href="#i-pin"/></svg> Musterstr. 123<br>
      12345 Musterstadt
    </div>
    <div class="footer-col footer-col--contact">
      <svg class="icon" width="5" height="5"><use href="#i-phone"/></svg> 010 - 123 456789<br>
      <svg class="icon" width="5" height="5"><use href="#i-mail"/></svg> info@website.com<br>
      &nbsp;&nbsp;www.website.com
    </div>
    <div class="footer-col footer-col--bank">
      Musterbank gmbh<br>
      IBAN: DE12345677890<br>
      BIC: MUS940DS90
    </div>
  </footer>
</section>

<section class="card card--front">
  <div class="card__head">
    <div class="wordmark"><span class="wordmark__square"></span>Braukon Solutions</div>
  </div>
  <div class="card__details">
    <div>Name Vorname &nbsp;<span class="accent">Geschäftsführer</span></div>
    <div class="row" style="margin-top:5px"><svg class="icon" width="7" height="7"><use href="#i-pin"/></svg>Musterstr. 123 <span class="accent">•</span> 12345 Musterstadt</div>
    <div class="row"><svg class="icon" width="7" height="7"><use href="#i-mail"/></svg>info@webseite.com &nbsp;<svg class="icon" width="7" height="7"><use href="#i-phone"/></svg>+49 (0) 10 - 234 567-8</div>
    <div class="web">www.webseite.com</div>
  </div>
</section>

<section class="card card--back">
  <div class="wordmark wordmark--light"><span class="wordmark__square"></span>Braukon Solutions</div>
</section>

</body>
</html>
```